Iron Ridge Roofing Business Card

Need a business card with the logo that was designed here

Contact Information for Business Card

Name, Title, Phone, Email, Website, Company name

```html
<!DOCTYPE html>
<html lang="en">
<head>
<meta charset="utf-8">
<title>Iron Ridge Roofing – Business Card</title>
<link href="https://fonts.googleapis.com/css2?family=Montserrat:wght@500;700&display=swap" rel="stylesheet">
<style>
  :root {
    --page-bg: #3a3a3a;
    --card-white: #ffffff;
    --card-black: #121212;
    --brand-blue: #1f78c4;
    --brand-grey: #8e9096;
    --ink: #1b1b1b;
    --emboss: #3c3c3c;
  }
  * { margin: 0; padding: 0; box-sizing: border-box; }
  html, body { width: 1200px; height: 1200px; overflow: hidden; }
  body {
    background: var(--page-bg);
    font-family: "Montserrat", sans-serif;
    position: relative;
  }
  .card {
    position: absolute;
    width: 700px;
    height: 400px;
    border-radius: 36px;
    overflow: hidden;
    box-shadow: 0 18px 40px rgba(0,0,0,0.45);
  }
  .card--front { left: 110px; top: 120px; background: var(--card-white); }
  .card--back {
    left: 390px; top: 660px; background: var(--card-black);
    border-bottom: 4px solid var(--brand-blue);
  }
  .brand-name {
    position: absolute;
    display: flex;
    align-items: center;
    gap: 14px;
    font-weight: 700;
    letter-spacing: 1px;
    white-space: nowrap;
  }
  .brand-name__mark { width: 18px; height: 18px; }
  .card--front .brand-name {
    right: 60px; top: 110px; font-size: 34px; color: var(--brand-blue);
  }
  .card--front .brand-name__mark { background: var(--brand-grey); }
  .card--back .brand-name {
    left: 50%; top: 50%; transform: translate(-50%, -50%);
    font-size: 44px; color: var(--emboss);
  }
  .card--back .brand-name__mark { background: var(--emboss); width: 22px; height: 22px; }
  .holder { position: absolute; left: 56px; top: 210px; }
  .holder__name {
    font-size: 32px; font-weight: 700; color: var(--brand-blue);
    line-height: 1; letter-spacing: 0.5px;
  }
  .holder__role {
    font-size: 16px; font-weight: 500; color: var(--ink);
    letter-spacing: 1px; margin-top: 4px;
  }
  .contact-list { list-style: none; margin-top: 16px; }
  .contact-list li {
    display: flex; align-items: center; gap: 12px;
    font-size: 19px; font-weight: 500; color: var(--ink);
    margin-bottom: 6px;
  }
  .contact-list svg { width: 20px; height: 20px; flex: none; }
  .band { position: absolute; bottom: 0; height: 24px; }
  .band--blue { left: 0; width: 430px; background: var(--brand-blue); }
  .band--grey { left: 440px; right: 0; background: var(--brand-grey); }
</style>
</head>
<body>
  <section class="card card--front">
    <div class="brand-name"><span class="brand-name__mark"></span>Iron Ridge Roofing</div>

    <div class="holder">
      <p class="holder__name">FULL NAME</p>
      <p class="holder__role">POSITION</p>
      <ul class="contact-list">
        <li>
          <svg viewBox="0 0 24 24" aria-hidden="true"><path fill="#1f78c4" d="M6.6 10.8a15.1 15.1 0 0 0 6.6 6.6l2.2-2.2c.3-.3.7-.4 1-.2 1.1.4 2.3.6 3.6.6.6 0 1 .4 1 1V20c0 .6-.4 1-1 1A17 17 0 0 1 3 4c0-.6.4-1 1-1h3.5c.6 0 1 .4 1 1 0 1.3.2 2.5.6 3.6.1.3 0 .7-.2 1z"/></svg>
          (000) 000 0000
        </li>
        <li>
          <svg viewBox="0 0 24 24" aria-hidden="true"><rect x="2" y="5" width="20" height="14" fill="#1f78c4"/><path d="M2 5l10 8 10-8M2 19l7-7M22 19l-7-7" stroke="#fff" stroke-width="1.6" fill="none"/></svg>
          email@company.com
        </li>
        <li>
          <svg viewBox="0 0 24 24" aria-hidden="true"><g fill="none" stroke="#1f78c4" stroke-width="1.8"><circle cx="12" cy="12" r="9.5"/><ellipse cx="12" cy="12" rx="4" ry="9.5"/><path d="M2.5 12h19M4 7h16M4 17h16"/></g></svg>
          www.company.com
        </li>
      </ul>
    </div>

    <div class="band band--blue"></div>
    <div class="band band--grey"></div>
  </section>

  <section class="card card--back">
    <div class="brand-name"><span class="brand-name__mark"></span>Iron Ridge Roofing</div>
  </section>
</body>
</html>
```